Icons for Workspaces for a financial CRM

We need several icons to indicate personal workspaces for different type of user(s) of our SaaS-based CRM.
We offer a front- and middle-office management software for the alternative assets industry - private equity, hedge funds, real estate, institutional investors, etc - thourgh our proprietary software called Velquor. The company's main office is in Boston.
The workspaces in question represent personalized Home pages, based on the user persona - there is a workspace for Investor Relations people, another for Deal Management people, etc. There is also a "My Home" workspace where the user can arrange their own informatation. One user can have access to sevaral workspaces, they are not limited to just one.
The buttons that will point the user the workspaces, will be placed on top left position of the screen, one under the other, as a list. The icons will be coupled with text.
Here is the list of all workspaces for which we need icons - a total of 8 icons (with explanations):
• My Home
(personalized home workspace for the logged in user)
• Fundraising
Raising money for a fund.
• Investor Relations
The management of existing client relationships
• Deal Management
The management of new investments
• Portfolio Management
The management of existing investments
• Research Management
The gathering of information about the market, industry trends, innovations, etc.
• Resource Management
The management of people resources
• Portal Management
Managing of user accounts for our investor portal. This is setting up new users, editing existing users, and deactivating prior users.
The default colors of the Velquor application are light-blue and light-grey, but we also provide different skins, so it will be good to see a couple of versions, in different colors.
Size - 32 x 32 pixels
Target Market(s)
People who work in the financial industry.
Industry/Entity Type
Financial

```html
<!DOCTYPE html>
<html lang="en">
<head>
<meta charset="utf-8">
<title>Workspace Icons</title>
<link href="https://fonts.googleapis.com/css2?family=Open+Sans:wght@600&display=swap" rel="stylesheet">
<style>
  :root {
    --bg-top: #c9c9c9;
    --bg-light: #ffffff;
    --bg-bottom: #a3a3a3;
    --tile-light: #8cd0ff;
    --tile-mid: #3ea4f6;
    --tile-dark: #1a7fe6;
    --label: #1d6fc8;
    --glyph: #ffffff;
  }
  html, body {
    margin: 0;
    padding: 0;
    overflow: hidden;
  }
  .canvas {
    position: relative;
    width: 1200px;
    height: 255px;
    overflow: hidden;
    background: linear-gradient(to bottom,
      var(--bg-top) 0%,
      var(--bg-light) 22%,
      var(--bg-light) 58%,
      var(--bg-bottom) 100%);
    font-family: "Open Sans", Arial, sans-serif;
  }
  .defs { position: absolute; width: 0; height: 0; }
  .workspace {
    position: absolute;
    top: 74px;
    width: 140px;
    margin-left: -70px;
    text-align: center;
  }
  .workspace-icon {
    display: block;
    width: 70px;
    height: 64px;
    margin: 0 auto 0 42px;
  }
  .workspace-label {
    display: block;
    margin-top: var(--label-gap, 30px);
    color: var(--label);
    font-size: 12.5px;
    line-height: 16px;
    font-weight: 600;
    text-transform: uppercase;
  }
</style>
</head>
<body>
<div class="canvas">
  <svg class="defs" aria-hidden="true">
    <defs>
      <linearGradient id="tile-fill" x1="0" y1="0" x2="0" y2="1">
        <stop offset="0" stop-color="var(--tile-light)"/>
        <stop offset="0.45" stop-color="var(--tile-mid)"/>
        <stop offset="1" stop-color="var(--tile-dark)"/>
      </linearGradient>
      <radialGradient id="tile-shadow" cx="0.5" cy="0.5" r="0.5">
        <stop offset="0" stop-color="#000" stop-opacity="0.28"/>
        <stop offset="1" stop-color="#000" stop-opacity="0"/>
      </radialGradient>
      <g id="tile">
        <ellipse cx="34" cy="55" rx="34" ry="5" fill="url(#tile-shadow)"/>
        <rect x="3" y="3" width="54" height="54" rx="9" fill="url(#tile-fill)"/>
        <path d="M12 3 H48 A9 9 0 0 1 57 12 V18 L3 40 V12 A9 9 0 0 1 12 3Z" fill="#fff" opacity="0.22"/>
        <rect x="3.5" y="3.5" width="53" height="53" rx="8.5" fill="none" stroke="#fff" stroke-opacity="0.35"/>
      </g>
    </defs>
  </svg>

  <div class="workspace" style="left:92px">
    <svg class="workspace-icon" viewBox="0 0 70 64" aria-hidden="true">
      <use href="#tile"/>
      <path d="M30 16 L45 30 H41 V43 H34 V35 H27 V43 H20 V30 H15Z" fill="var(--glyph)"/>
    </svg>
    <span class="workspace-label" style="--label-gap:34px">Home</span>
  </div>

  <div class="workspace" style="left:226px">
    <svg class="workspace-icon" viewBox="0 0 70 64" aria-hidden="true">
      <use href="#tile"/>
      <path d="M25 13 L35 13 L32 20 L28 20Z" fill="var(--glyph)"/>
      <path d="M28 21 C18 27 16 35 17 40 C18 46 24 47 30 47 C36 47 42 46 43 40 C44 35 42 27 32 21Z" fill="var(--glyph)"/>
      <text x="30" y="41" text-anchor="middle" font-family="Arial, sans-serif" font-weight="700" font-size="16" fill="var(--tile-dark)">$</text>
    </svg>
    <span class="workspace-label" style="--label-gap:35px">Fundraising</span>
  </div>

  <div class="workspace" style="left:373px">
    <svg class="workspace-icon" viewBox="0 0 70 64" aria-hidden="true">
      <use href="#tile"/>
      <circle cx="22" cy="26" r="5" fill="var(--glyph)"/>
      <path d="M13 48 V39 C13 34 17 32 22 32 C27 32 31 34 31 39 V48Z" fill="var(--glyph)"/>
      <circle cx="38" cy="20" r="5" fill="var(--glyph)"/>
      <path d="M30 42 V33 C30 28 33 26 38 26 C43 26 47 28 47 33 V42Z" fill="var(--glyph)"/>
      <path d="M37 27 L39 27 L40 36 L38 39 L36 36Z" fill="var(--tile-dark)"/>
    </svg>
    <span class="workspace-label" style="--label-gap:33px">Investor<br>Relations</span>
  </div>

  <div class="workspace" style="left:512px">
    <svg class="workspace-icon" viewBox="0 0 70 64" aria-hidden="true">
      <use href="#tile"/>
      <path d="M8 26 L18 22 L28 26 L38 23 L52 30 L50 34 L36 30 L40 36 L34 40 L28 36 L24 40 L18 36 L10 34Z" fill="var(--glyph)"/>
      <path d="M26 28 L34 26 L44 36 L40 39 L32 32Z" fill="var(--tile-mid)" opacity="0.6"/>
    </svg>
    <span class="workspace-label" style="--label-gap:30px">Deal<br>Management</span>
  </div>

  <div class="workspace" style="left:659px">
    <svg class="workspace-icon" viewBox="0 0 70 64" aria-hidden="true">
      <use href="#tile"/>
      <path d="M25 22 V18 H35 V22" fill="none" stroke="var(--glyph)" stroke-width="2.5"/>
      <rect x="14" y="22" width="32" height="22" rx="2" fill="var(--glyph)"/>
      <rect x="14" y="30" width="32" height="2" fill="var(--tile-mid)"/>
      <rect x="28" y="29" width="4" height="4" fill="var(--glyph)" stroke="var(--tile-mid)"/>
    </svg>
    <span class="workspace-label" style="--label-gap:32px">Portfolio<br>Management</span>
  </div>

  <div class="workspace" style="left:797px">
    <svg class="workspace-icon" viewBox="0 0 70 64" aria-hidden="true">
      <use href="#tile"/>
      <path d="M11 24 H21 L24 27 H39 V46 H11Z" fill="var(--glyph)"/>
      <path d="M11 46 L16 33 H44 L39 46Z" fill="var(--tile-mid)" stroke="var(--glyph)" stroke-width="2"/>
      <circle cx="40" cy="22" r="6" fill="none" stroke="var(--glyph)" stroke-width="3"/>
      <path d="M36 26 L28 35" stroke="var(--glyph)" stroke-width="3.5" stroke-linecap="round"/>
    </svg>
    <span class="workspace-label" style="--label-gap:33px">Research<br>Management</span>
  </div>

  <div class="workspace" style="left:937px">
    <svg class="workspace-icon" viewBox="0 0 70 64" aria-hidden="true">
      <use href="#tile"/>
      <circle cx="30" cy="30" r="13" fill="none" stroke="var(--glyph)" stroke-width="2.5"/>
      <g stroke="var(--glyph)" stroke-width="1.5">
        <path d="M30 19 V21 M30 39 V41 M19 30 H21 M39 30 H41"/>
      </g>
      <path d="M30 30 L30 23 M30 30 L35 33" stroke="var(--glyph)" stroke-width="2" stroke-linecap="round"/>
    </svg>
    <span class="workspace-label" style="--label-gap:33px">Resource<br>Management</span>
  </div>

  <div class="workspace" style="left:1081px">
    <svg class="workspace-icon" viewBox="0 0 70 64" aria-hidden="true">
      <use href="#tile"/>
      <circle cx="22" cy="22" r="7" fill="none" stroke="var(--glyph)" stroke-width="4"/>
      <path d="M27 27 L44 44" stroke="var(--glyph)" stroke-width="4" stroke-linecap="round"/>
      <path d="M36 36 L40 32 M40 40 L44 36" stroke="var(--glyph)" stroke-width="3.5" stroke-linecap="round"/>
    </svg>
    <span class="workspace-label" style="--label-gap:33px">Portal<br>Management</span>
  </div>
</div>
</body>
</html>
```